Providing Back Office Solutions to Financial Advisors and Attorney Needs a Business Card Design

Need a Business Card Design that speaks to Financial Advisor and Attorneys. Some of the word that come to mind is Clean/Simple & Futuristic.

Industry/Entity Type

Business

```html
<!DOCTYPE html>
<html lang="en">
<head>
<meta charset="utf-8">
<title>Verantis Back Office Solutions – Business Card</title>
<link rel="stylesheet" href="https://fonts.googleapis.com/css2?family=Open+Sans:wght@400;600&family=Oswald:wght@600&display=swap">
<style>
  :root {
    --stage: #1c1c1e;
    --card-white: #ffffff;
    --brand-blue: #1f7fc0;
    --brand-blue-light: #2b93d6;
    --brand-blue-deep: #176aa6;
    --navy: #2a4a8c;
    --text-grey: #5a5a5a;
    --rule-grey: #9a9a9a;
  }
  * { box-sizing: border-box; margin: 0; padding: 0; }
  html, body { width: 1200px; height: 904px; overflow: hidden; }
  body {
    background: var(--stage);
    font-family: "Open Sans", sans-serif;
    position: relative;
  }
  .card {
    position: absolute;
    left: 290px;
    width: 620px;
    height: 354px;
    border-radius: 2px;
    overflow: hidden;
  }
  /* Back side */
  .card-back { top: 56px; }
  .back-pattern {
    position: absolute; inset: 0;
    background: radial-gradient(ellipse at 45% 45%, var(--brand-blue-light) 0%, var(--brand-blue) 55%, var(--brand-blue-deep) 100%);
  }
  .back-brand {
    position: absolute; left: 0; right: 0; top: 148px;
    text-align: center; color: var(--card-white);
  }
  .back-brand .brand-name {
    font-weight: 600; font-size: 34px; letter-spacing: 5px; line-height: 1;
  }
  .back-brand .brand-tagline {
    font-size: 11px; letter-spacing: 0.5px; margin-top: 6px;
  }
  /* Front side */
  .card-front { top: 494px; background: var(--card-white); }
  .front-logo {
    position: absolute; top: 58px; left: 0; right: 0;
    display: flex; justify-content: center; align-items: center; gap: 12px;
  }
  .logo-square { width: 40px; height: 40px; background: var(--brand-blue); }
  .logo-divider { width: 1px; height: 48px; background: var(--navy); }
  .logo-text .brand-name {
    color: var(--brand-blue-deep); font-weight: 600; font-size: 32px;
    letter-spacing: 4px; line-height: 1;
  }
  .logo-text .brand-tagline {
    color: var(--brand-blue); font-size: 11px; letter-spacing: 0.4px; margin-top: 3px;
  }
  .front-details {
    position: absolute; top: 156px; left: 0; right: 0;
    display: flex; justify-content: center; align-items: center; gap: 22px;
  }
  .person { text-align: right; }
  .person-name {
    font-family: "Oswald", sans-serif; font-weight: 600; font-size: 34px;
    color: var(--brand-blue); line-height: 1; letter-spacing: 0.5px;
  }
  .person-title { font-size: 13px; color: var(--text-grey); margin-top: 2px; }
  .details-divider { width: 1px; height: 62px; background: var(--rule-grey); }
  .contact-list { list-style: none; }
  .contact-list li {
    display: flex; align-items: center; gap: 10px;
    font-size: 14px; color: var(--text-grey); line-height: 21px;
  }
  .contact-list svg { width: 12px; height: 12px; flex: none; }
  .address {
    position: absolute; bottom: 58px; left: 0; right: 0;
    text-align: center; font-size: 14px; color: var(--text-grey);
  }
</style>
</head>
<body>
  <section class="card card-back">
    <div class="back-pattern" role="img" aria-label="Blue background with a faint repeating pattern of the brand mark"></div>
    <div class="back-brand">
      <div class="brand-name">VERANTIS</div>
      <div class="brand-tagline">BACK OFFICE SOLUTIONS</div>
    </div>
  </section>

  <section class="card card-front">
    <div class="front-logo">
      <div class="logo-square"></div>
      <div class="logo-divider"></div>
      <div class="logo-text">
        <div class="brand-name">VERANTIS</div>
        <div class="brand-tagline">BACK OFFICE SOLUTIONS</div>
      </div>
    </div>

    <div class="front-details">
      <div class="person">
        <div class="person-name">DANIEL MARSH</div>
        <div class="person-title">Manager</div>
      </div>
      <div class="details-divider"></div>
      <ul class="contact-list">
        <li>
          <svg viewBox="0 0 12 12" aria-hidden="true"><path d="M2.5 1 L4.5 1 L5 3.5 L3.8 4.4 C4.4 5.8 5.9 7.4 7.6 8.2 L8.5 7 L11 7.5 L11 9.5 C11 10.3 10.3 11 9.5 11 C5 11 1 7 1 2.5 C1 1.7 1.7 1 2.5 1 Z" fill="#2b93d6"/></svg>
          +111 2040 3060
        </li>
        <li>
          <svg viewBox="0 0 12 12" aria-hidden="true"><rect x="0.5" y="2" width="11" height="8" rx="1" fill="#2b93d6"/><path d="M1 2.6 L6 6.6 L11 2.6" stroke="#fff" stroke-width="1" fill="none"/></svg>
          hello@verantisoffice.com
        </li>
        <li>
          <svg viewBox="0 0 12 12" aria-hidden="true"><circle cx="6" cy="6" r="5.5" fill="#2b93d6"/><path d="M0.5 6 H11.5 M6 0.5 C3.5 3.5 3.5 8.5 6 11.5 M6 0.5 C8.5 3.5 8.5 8.5 6 11.5" stroke="#fff" stroke-width="0.8" fill="none"/></svg>
          www.verantisoffice.com
        </li>
      </ul>
    </div>

    <div class="address">42 Harbor Lane, Westfield Park, CA 904215.</div>
  </section>
</body>
</html>
```